First North America Product Category Rule

8 x 10 foot booth design for a stretch fabric wrap-around. The booth will be used in a very small exhibit area for 150 attendees. It is for the packaging industry focused on the environment. This booth graphic is NOT about our company, but to promote participation in a project we are sponsoring. The project is to develop the first North American Packaging Category Rule, so the booth is to invite conference attendees to join our effort. Production specifications are attached.

Target Market(s)

Meridian 300, Sustainability Directors, Packaging Engineers

Industry/Entity Type

Packaging; Environment

Font styles to use
Sans Serif

Requirements
Must have
• An Eye-Catching or Intriguing Image/Graphics/Letter Treatment
Should not have
• Nothing too bright or garish. All text should be above waist height (No text below the 36-40" mark)

```html
<!DOCTYPE html>
<html lang="en">
<head>
<meta charset="utf-8">
<title>First North American PCR for Protective Packaging</title>
<link rel="stylesheet" href="https://fonts.googleapis.com/css2?family=Merriweather:ital,wght@0,400;0,700;0,900;1,700&family=Oswald:wght@600&display=swap">
<style>
  :root {
    --stage: #000000;
    --paper: #ffffff;
    --mist: #eef0f4;
    --teal: #2fc0b2;
    --teal-deep: #23a99d;
    --indigo: #5a63c4;
    --ink: #111111;
    --night: #1f2a3a;
    --ribbon-yellow: #f6efa3;
    --white: #ffffff;
  }
  * { margin: 0; padding: 0; box-sizing: border-box; }
  html, body { width: 1200px; height: 737px; overflow: hidden; background: var(--stage); }
  .canvas { position: relative; width: 1200px; height: 737px; font-family: "Merriweather", Georgia, serif; }
  .artwork { position: absolute; left: 0; top: 0; width: 1200px; height: 737px; }
  .headline {
    position: absolute; right: 608px; top: 146px; text-align: right;
    color: var(--teal); font-weight: 900; font-size: 40px; line-height: 44px;
  }
  .rule-line { position: absolute; left: 184px; width: 505px; height: 2px; background: var(--ink); }
  .rule-top { top: 313px; }
  .rule-bottom { top: 449px; }
  .title-block { position: absolute; right: 511px; top: 322px; text-align: right; color: var(--ink); }
  .title-kicker { font-style: italic; font-weight: 700; font-size: 23px; line-height: 30px; }
  .title-main { font-weight: 900; font-size: 35px; line-height: 47px; }
  .sponsor {
    position: absolute; left: 471px; top: 502px; color: var(--ink);
    font-weight: 900; font-size: 17px; line-height: 22px;
  }
  .sign-up {
    position: absolute; left: 200px; top: 126px; width: 113px; text-align: center;
    font-family: "Oswald", "Arial Narrow", sans-serif; font-weight: 600;
    font-size: 31px; line-height: 34px; color: var(--teal-deep); letter-spacing: 0.3px;
  }
  .quote {
    position: absolute; left: 746px; top: 473px; width: 250px; text-align: center;
    color: var(--white); font-size: 14.5px; line-height: 19.3px;
  }
  .step-label { font-family: "Merriweather", Georgia, serif; font-size: 8px; font-weight: 700; fill: var(--white); }
  .step-number { font-family: "Merriweather", Georgia, serif; font-size: 15px; font-weight: 900; fill: var(--white); }
</style>
</head>
<body>
<div class="canvas">
  <svg class="artwork" viewBox="0 0 1200 737" xmlns="http://www.w3.org/2000/svg">
    <defs>
      <linearGradient id="swoosh" x1="0" y1="0" x2="0.3" y2="1">
        <stop offset="0" stop-color="#2fc0b2"/>
        <stop offset="0.55" stop-color="#3aa7b8"/>
        <stop offset="1" stop-color="#5a63c4"/>
      </linearGradient>
      <linearGradient id="photo-tone" x1="0" y1="0" x2="1" y2="1">
        <stop offset="0" stop-color="#6f6a68"/>
        <stop offset="0.45" stop-color="#a88d73"/>
        <stop offset="1" stop-color="#7e7670"/>
      </linearGradient>
      <linearGradient id="segment" x1="0" y1="0" x2="1" y2="1">
        <stop offset="0" stop-color="#2fc0b2"/>
        <stop offset="1" stop-color="#5b5fc7"/>
      </linearGradient>
      <linearGradient id="ribbon-tone" x1="0" y1="0" x2="0" y2="1">
        <stop offset="0" stop-color="#4f7fc4"/>
        <stop offset="1" stop-color="#3cb3b4"/>
      </linearGradient>
      <clipPath id="panel-clip"><rect x="175" y="137" width="1214" height="685"/></clipPath>
    </defs>

    <g class="booth-panel" transform="translate(134 105) scale(0.7676) translate(-175 -137)" clip-path="url(#panel-clip)">
      <rect x="175" y="137" width="1214" height="685" fill="var(--paper)"/>
      <path d="M 820 137 C 620 220, 470 450, 560 822 L 640 822 C 560 520, 650 300, 870 137 Z" fill="var(--mist)"/>
      <path d="M 1195 137 L 1389 137 L 1389 822 L 900 822 C 830 720, 775 560, 790 400 C 805 270, 960 160, 1195 137 Z" fill="url(#swoosh)"/>
      <path role="img" aria-label="Photo: warehouse worker in hard hat lifting a cardboard box onto shelving"
            d="M 1040 137 L 1389 137 L 1389 712 C 1360 700, 1335 680, 1320 650 L 1150 590 C 1050 560, 960 480, 930 380 C 915 290, 960 200, 1040 137 Z"
            fill="url(#photo-tone)"/>
      <path d="M 940 822 L 940 660 Q 940 615 985 600 L 1100 562 Q 1135 550 1170 562 L 1288 600 Q 1332 615 1332 660 L 1332 822 Z" fill="var(--night)"/>
    </g>

    <g class="sign-up-badge">
      <rect x="209" y="105" width="94" height="14" fill="var(--teal)"/>
      <rect role="img" aria-label="Illustration: rolled scroll ribbon" x="185" y="200" width="119" height="92" rx="16" fill="url(#ribbon-tone)"/>
      <rect x="200" y="119" width="113" height="88" fill="var(--ribbon-yellow)"/>
    </g>

    <g class="process-arc" transform="translate(322 606)" stroke="var(--white)" stroke-width="2">
      <path d="M -127 0 A 127 127 0 0 1 -89.8 -89.8 L -38.2 -38.2 A 54 54 0 0 0 -54 0 Z" fill="url(#segment)"/>
      <path transform="rotate(45)" d="M -127 0 A 127 127 0 0 1 -89.8 -89.8 L -38.2 -38.2 A 54 54 0 0 0 -54 0 Z" fill="url(#segment)"/>
      <path transform="rotate(90)" d="M -127 0 A 127 127 0 0 1 -89.8 -89.8 L -38.2 -38.2 A 54 54 0 0 0 -54 0 Z" fill="url(#segment)"/>
      <path transform="rotate(135)" d="M -127 0 A 127 127 0 0 1 -89.8 -89.8 L -38.2 -38.2 A 54 54 0 0 0 -54 0 Z" fill="url(#segment)"/>
    </g>

    <g class="process-labels">
      <text class="step-label" text-anchor="end"><tspan x="259" y="566">PCR</tspan><tspan x="259" y="577">Priduct</tspan><tspan x="259" y="588">Category</tspan><tspan x="259" y="599">rules</tspan></text>
      <text class="step-label" text-anchor="end"><tspan x="312" y="522">LCA</tspan><tspan x="312" y="533">Life Cycle</tspan><tspan x="312" y="544">Assessment</tspan></text>
      <text class="step-label"><tspan x="329" y="522">Third</tspan><tspan x="329" y="533">Party</tspan><tspan x="329" y="544">Verification</tspan></text>
      <text class="step-label"><tspan x="378" y="578">EPD</tspan><tspan x="378" y="589">Registration</tspan><tspan x="378" y="600">and Publication</tspan></text>
    </g>

    <g class="process-steps">
      <circle cx="199.5" cy="562" r="19" fill="url(#segment)" stroke="var(--white)" stroke-width="3"/>
      <text class="step-number" x="199.5" y="567.5" text-anchor="middle">01</text>
      <circle cx="268.5" cy="492" r="19" fill="url(#segment)" stroke="var(--white)" stroke-width="3"/>
      <text class="step-number" x="268.5" y="497.5" text-anchor="middle">02</text>
      <circle cx="367" cy="492" r="19" fill="url(#segment)" stroke="var(--white)" stroke-width="3"/>
      <text class="step-number" x="367" y="497.5" text-anchor="middle">03</text>
      <circle cx="439" cy="557" r="19" fill="url(#segment)" stroke="var(--white)" stroke-width="3"/>
      <text class="step-number" x="439" y="562.5" text-anchor="middle">04</text>
    </g>
  </svg>

  <div class="sign-up">SIGN UP<br>NOW</div>

  <h1 class="headline">Enlisting<br>Stakeholder<br>Participation</h1>

  <div class="rule-line rule-top"></div>
  <div class="title-block">
    <p class="title-kicker">First North American</p>
    <h2 class="title-main">Product Category Rule (PCR)<br>For Protective Packaging</h2>
  </div>
  <div class="rule-line rule-bottom"></div>

  <p class="sponsor">Sponsored by<br>Foam Packaging<br>Council Managed<br>by Clear Ledger<br>Group</p>

  <p class="quote">“How EPD Can Move the<br>Dialogue Beyond End-of-Life<br>Disposal to Include<br>Environmental Benchmarks<br>for Product Production &amp;<br>Distribution”</p>
</div>
</body>
</html>
```